Million Dollar Vehicle Design For Home Service Company

New design for Bright-Path Servicemen (home service company) vehicles.

Both sides and back

We are a new (opening in about 30 days) home service company.

We will begin by offering residential electrical services and soon expand to a full line by adding handyman, heating, cooling. plumbing and drain cleaning.

Looking for simple. Not cluttered.

Minimalist - Less is More mindset, but it must catch the eye.

Here is a link the website prototype being built for us. It has a bit more stuff on it now than it will in its final version, but this will help you get a feel for the colors.

http://www.lanternquaydigital.com/PROOF/brightpath-servicemen-4/

You may also find inspiration at cozyvantrel.com

**Also, please note that some of the attached files will differ from my requests due to changes being made as we get closer to opening. For example, the tagline is different.

Target Market(s)

Home Owners 35 - 65 years old.

Industry/Entity Type

Electrician

Font styles to use
Serif

Requirements
Must have
• Simple. Easy to read. Easy to understand what the company does and how to contact.
• Big Website
• Big Phone Number
• Big Name
• Website: MyBrightPathPro.com
• Phone number: 555-014-2287
• ***Tagline: Bright-Path, Each Visit or You'll Save $39
• ***Please note the tagline in this brief is different than is in the attached image.
Nice to have
• We will be adding services in the future. It would be nice to consider how these will be displayed on the vehicle. For example, it should be listed that we provide expert electrical services. I want to be able to list other services such as plumbing, heating and cooling as we add them by modifying only few things on each vehicle.
Should not have
• Cluttered. Should not be difficult to understand within 1 second.

```html
<!DOCTYPE html>
<html lang="en">
<head>
<meta charset="utf-8">
<title>Bright-Path Servicemen – Vehicle Wrap</title>
<link rel="stylesheet" href="https://fonts.googleapis.com/css2?family=Montserrat:ital,wght@0,600;0,700;0,800;1,600;1,700&family=Oswald:wght@700&display=swap">
<style>
  :root{
    --paper:#ffffff;
    --body:#f7f7f7;
    --outline:#c9c9c9;
    --orange:#f0461e;
    --ink:#141414;
    --glass:#2b2f33;
    --tyre:#1b1b1b;
    --rim:#cfd3d6;
    --hub:#8d9296;
    --lime:#7cc242;
    --mascot-tone:#e8693f;
  }
  *{margin:0;padding:0;box-sizing:border-box}
  html,body{width:1200px;height:1200px;overflow:hidden;background:var(--paper)}
  .sheet{width:1200px;height:1200px;display:flex;flex-direction:column;justify-content:center;align-items:center;gap:70px}
  .van{width:1060px;height:445px;display:block}
  .tagline-small{font-family:"Montserrat",sans-serif;font-style:italic;font-weight:700;font-size:13px;fill:var(--ink)}
  .tagline-small .price{fill:var(--lime)}
  .category{font-family:"Montserrat",sans-serif;font-style:italic;font-weight:600;font-size:32px;fill:var(--orange)}
  .phone{font-family:"Montserrat",sans-serif;font-weight:700;font-size:27px;fill:var(--paper)}
  .brand-name{font-family:"Oswald",sans-serif;font-weight:700;font-size:36px;fill:var(--ink)}
  .brand-sub{font-family:"Oswald",sans-serif;font-weight:700;font-size:20px;fill:var(--ink);letter-spacing:1px}
  .service{font-family:"Montserrat",sans-serif;font-weight:800;font-size:15px;fill:var(--paper);letter-spacing:.5px}
  .website{font-family:"Montserrat",sans-serif;font-weight:700;font-size:17px;fill:var(--paper)}
</style>
</head>
<body>
<main class="sheet">

  <!-- Electrical-only layout -->
  <svg class="van van--electrical" viewBox="0 0 1000 420" aria-label="Bright-Path Servicemen van side, electrical services">
    <defs>
      <clipPath id="body-clip">
        <path d="M40,335 L22,305 L24,222 Q32,192 92,178 L212,62 Q242,28 302,24 L958,18 Q986,20 989,62 L992,305 Q992,330 975,335 Z"/>
      </clipPath>
      <linearGradient id="rear-fade" x1="0" x2="1">
        <stop offset="0" stop-color="#b23a1a" stop-opacity="0"/>
        <stop offset="1" stop-color="#8a2a14"/>
      </linearGradient>
      <symbol id="van-shell" viewBox="0 0 1000 420">
        <path class="van-body" d="M40,335 L22,305 L24,222 Q32,192 92,178 L212,62 Q242,28 302,24 L958,18 Q986,20 989,62 L992,305 Q992,330 975,335 Z" fill="var(--body)" stroke="var(--outline)" stroke-width="2"/>
        <g clip-path="url(#body-clip)">
          <path class="swoosh-upper" d="M200,150 Q380,50 720,18 L640,18 Q400,40 220,120 Z" fill="var(--orange)"/>
          <path class="band-main" d="M170,260 Q330,150 560,118 L1000,92 L1000,170 L640,172 Q420,178 300,250 Z" fill="var(--orange)"/>
          <path class="band-lower" d="M340,290 Q420,230 560,222 L760,226 L760,262 L560,262 Q440,266 380,300 Z" fill="var(--ink)"/>
          <rect class="rocker" x="330" y="300" width="470" height="30" fill="var(--ink)"/>
          <rect class="rear-texture" x="905" y="210" width="90" height="125" fill="url(#rear-fade)"/>
          <rect class="bumper-front" x="18" y="290" width="90" height="45" fill="var(--ink)"/>
        </g>
        <path class="window-cab" d="M228,78 Q250,55 300,52 L335,52 L335,150 L180,155 Z" fill="var(--glass)"/>
        <path class="headlight" d="M28,230 Q50,205 95,198 L90,218 Q55,224 30,245 Z" fill="#9aa0a4"/>
        <line class="door-seam" x1="345" y1="40" x2="345" y2="330" stroke="var(--outline)" stroke-width="1.5"/>
        <line class="door-seam" x1="800" y1="30" x2="800" y2="330" stroke="var(--outline)" stroke-width="1.5"/>
        <path class="arch" d="M80,335 A75,75 0 0 1 230,335 Z" fill="var(--ink)"/>
        <path class="arch" d="M760,335 A75,75 0 0 1 910,335 Z" fill="var(--ink)"/>
        <g class="wheel">
          <circle cx="155" cy="345" r="56" fill="var(--tyre)"/>
          <circle cx="155" cy="345" r="33" fill="var(--rim)"/>
          <circle cx="155" cy="345" r="10" fill="var(--hub)"/>
        </g>
        <g class="wheel">
          <circle cx="835" cy="345" r="56" fill="var(--tyre)"/>
          <circle cx="835" cy="345" r="33" fill="var(--rim)"/>
          <circle cx="835" cy="345" r="10" fill="var(--hub)"/>
        </g>
      </symbol>
    </defs>

    <use href="#van-shell"/>
    <g class="mascots" role="img" aria-label="Illustration of two cartoon technicians in orange shirts and caps">
      <rect x="362" y="80" width="100" height="212" rx="14" fill="var(--mascot-tone)" opacity=".85"/>
    </g>
    <text class="category" x="525" y="68" textLength="330" lengthAdjust="spacingAndGlyphs">home service company</text>
    <text class="brand-name" x="478" y="140" textLength="170" lengthAdjust="spacingAndGlyphs">BRIGHT-PATH</text>
    <text class="phone" x="735" y="138" textLength="180" lengthAdjust="spacingAndGlyphs">555-014-2287</text>
    <text class="brand-sub" x="479" y="170" textLength="120" lengthAdjust="spacingAndGlyphs">SERVICEMEN</text>
    <rect x="477" y="178" width="130" height="22" fill="var(--ink)"/>
    <text class="service" x="484" y="195" textLength="116" lengthAdjust="spacingAndGlyphs">ELECTRICIANS</text>
    <text class="tagline-small" x="740" y="196">Bright-Path, each visit</text>
    <text class="tagline-small" x="740" y="212">or you'll save <tspan class="price">$39</tspan> !</text>
    <text class="website" x="380" y="321">MyBrightPathPro.com</text>
  </svg>

  <!-- Full-service layout -->
  <svg class="van van--full" viewBox="0 0 1000 420" aria-label="Bright-Path Servicemen van side, full home services">
    <use href="#van-shell"/>
    <g class="mascots" role="img" aria-label="Illustration of two cartoon technicians in orange shirts and caps">
      <rect x="362" y="80" width="100" height="212" rx="14" fill="var(--mascot-tone)" opacity=".85"/>
    </g>
    <text class="category" x="525" y="68" textLength="330" lengthAdjust="spacingAndGlyphs">home service company</text>
    <text class="brand-name" x="478" y="140" textLength="170" lengthAdjust="spacingAndGlyphs">BRIGHT-PATH</text>
    <text class="phone" x="735" y="138" textLength="180" lengthAdjust="spacingAndGlyphs">555-014-2287</text>
    <text class="brand-sub" x="479" y="170" textLength="120" lengthAdjust="spacingAndGlyphs">SERVICEMEN</text>
    <rect x="477" y="178" width="130" height="22" fill="var(--ink)"/>
    <text class="service" x="484" y="195" textLength="116" lengthAdjust="spacingAndGlyphs">ELECTRICIANS</text>
    <rect x="500" y="203" width="118" height="22" fill="var(--ink)"/>
    <text class="service" x="514" y="220" textLength="90" lengthAdjust="spacingAndGlyphs">PLUMBING</text>
    <rect x="522" y="228" width="108" height="22" fill="var(--ink)"/>
    <text class="service" x="538" y="245" textLength="76" lengthAdjust="spacingAndGlyphs">HEATING</text>
    <rect x="546" y="253" width="110" height="22" fill="var(--ink)"/>
    <text class="service" x="562" y="270" textLength="78" lengthAdjust="spacingAndGlyphs">COOLING</text>
    <text class="tagline-small" x="740" y="196">Bright-Path, each visit</text>
    <text class="tagline-small" x="740" y="212">or you'll save <tspan class="price">$39</tspan> !</text>
    <text class="website" x="380" y="321">MyBrightPathPro.com</text>
  </svg>

</main>
</body>
</html>
```